Dalworth Pitching Mechanics

Private pitching sessions with a Division 1 PJTB baseball pitcher. Would also like a page setup where clients can request sesseions and pay for sessions.

```html
<!DOCTYPE html>
<html lang="en">
<head>
<meta charset="utf-8">
<title>Dalworth Pitching Mechanics</title>
<link href="https://fonts.googleapis.com/css2?family=Jost:ital,wght@0,400;0,600;0,700;1,800&display=swap" rel="stylesheet">
<style>
  :root {
    --brand-red: #ec1c24;
    --ink-dark: #0d0d0f;
    --white: #ffffff;
    --photo-deep: #15171c;
    --photo-mid: #3b3f47;
    --photo-warm: #6b4a36;
    --photo-turf: #26331f;
  }
  * { box-sizing: border-box; margin: 0; padding: 0; }
  html, body { width: 1200px; height: 675px; overflow: hidden; background: var(--ink-dark); }
  body { font-family: "Jost", "Futura", sans-serif; color: var(--white); }
  .page { position: relative; width: 1200px; height: 675px; overflow: hidden; }

  .site-header {
    position: absolute; left: 0; top: 0; width: 1200px; height: 94px;
    background: var(--brand-red);
    border-bottom: 3px solid var(--ink-dark);
    z-index: 2;
  }
  .brand-name {
    position: absolute; left: 96px; top: 22px;
    display: flex; align-items: center; gap: 8px;
    font-weight: 700; font-size: 34px; letter-spacing: 1px; color: var(--white);
  }
  .brand-dot { width: 12px; height: 12px; border-radius: 50%; background: var(--white); }

  .contact-bar {
    position: absolute; right: 114px; top: 16px;
    display: flex; align-items: center; gap: 30px;
    font-weight: 600; font-size: 19px;
  }
  .contact-item { display: flex; align-items: center; gap: 12px; white-space: nowrap; }
  .contact-item svg { fill: var(--ink-dark); }

  .main-nav {
    position: absolute; right: 114px; top: 51px;
    display: flex; align-items: center;
    font-weight: 600; font-size: 14px; white-space: nowrap;
  }
  .main-nav a { color: var(--white); text-decoration: none; }
  .nav-sep {
    display: inline-block; width: 2px; height: 18px; margin: 0 17px;
    background: var(--ink-dark); transform: skewX(-14deg);
  }

  .hero-photo {
    position: absolute; left: 0; top: 94px; width: 1200px; height: 581px;
    background:
      radial-gradient(ellipse 420px 380px at 760px 230px, rgba(120,40,40,0.35), transparent 70%),
      radial-gradient(ellipse 360px 300px at 1080px 120px, rgba(200,190,180,0.28), transparent 70%),
      radial-gradient(ellipse 520px 200px at 700px 560px, rgba(107,74,54,0.7), transparent 75%),
      linear-gradient(180deg, var(--photo-mid) 0%, var(--photo-deep) 45%, var(--photo-turf) 78%, var(--photo-deep) 100%);
  }
  .hero-photo::after {
    content: ""; position: absolute; inset: 0;
    background: linear-gradient(90deg, rgba(0,0,0,0.55) 0%, rgba(0,0,0,0.2) 55%, rgba(0,0,0,0.1) 100%);
  }

  .hero-copy { position: absolute; left: 169px; top: 228px; width: 520px; height: 300px; z-index: 1; }
  .hero-title {
    font-weight: 800; font-style: italic; font-size: 84px; line-height: 1;
    letter-spacing: 0.5px; white-space: nowrap;
  }
  .hero-subtitle {
    font-weight: 800; font-style: italic; font-size: 31px; line-height: 1;
    margin-top: 2px; white-space: nowrap;
  }
  .hero-text {
    margin: 30px 0 0 5px; width: 345px;
    font-weight: 400; font-size: 17.5px; line-height: 22.5px;
  }
  .cta {
    position: absolute; left: 5px; top: 240px;
    display: flex; align-items: center;
    text-decoration: none;
  }
  .cta-label {
    display: flex; align-items: center; justify-content: space-between;
    height: 54px; width: 178px; padding: 0 12px 0 18px;
    background: var(--brand-red);
    font-weight: 700; font-size: 23px; color: var(--white);
    white-space: nowrap; text-decoration: none;
  }
  .cta svg.cta-tail { display: block; }
</style>
</head>
<body>
<div class="page">
  <header class="site-header">
    <div class="brand-name"><span class="brand-dot"></span>DPM</div>

    <div class="contact-bar">
      <div class="contact-item">
        <svg width="19" height="14" viewBox="0 0 19 14" aria-hidden="true"><path d="M0 0h19v14H0z"/><path d="M1 1l8.5 7 8.5-7" stroke="#ec1c24" stroke-width="1.6" fill="none"/></svg>
        <span>info@dpmpitch.com</span>
      </div>
      <div class="contact-item">
        <svg width="14" height="19" viewBox="0 0 14 19" aria-hidden="true"><path d="M3 0l3 4-2 2c1 3 3 6 6 8l2-2 2 3-3 3C5 17 0 9 1 2z"/></svg>
        <span>+ 555 0142 376</span>
      </div>
    </div>

    <nav class="main-nav">
      <a href="#">About Us</a><span class="nav-sep"></span>
      <a href="#">Our Services</a><span class="nav-sep"></span>
      <a href="#">Gallery</a><span class="nav-sep"></span>
      <a href="#">Contacts</a>
    </nav>
  </header>

  <div class="hero-photo" role="img" aria-label="Baseball pitcher in a red jersey throwing from the mound in a floodlit stadium"></div>

  <section class="hero-copy">
    <h1 class="hero-title">DALWORTH</h1>
    <p class="hero-subtitle">PITCHING MECHANICS</p>
    <p class="hero-text">Lorem ipsum dolor sit amet, consectetur adipiscing elit, sed do eiusmod tempor incididunt ut labore et dolore magna aliqua.</p>
    <a class="cta" href="#">
      <span class="cta-label"><span>Get Started</span>
        <svg width="22" height="18" viewBox="0 0 22 18" aria-hidden="true"><path d="M2 2l7 7-7 7M11 2l7 7-7 7" stroke="#111" stroke-width="3.2" fill="none"/></svg>
      </span>
      <svg class="cta-tail" width="36" height="54" viewBox="0 0 36 54" aria-hidden="true">
        <path d="M0 0h6l20 27-20 27H0z" fill="#ec1c24"/>
        <path d="M4 0h4l20 27-20 27H4l20-27z" fill="#0d0d0f"/>
        <path d="M12 0h4l20 27-20 27h-4l20-27z" fill="#ec1c24"/>
      </svg>
    </a>
  </section>
</div>
</body>
</html>
```